Business Card Design Project

Design is for the business card of a holistic, integral therapist. Design is required for front (colour / pattern) and back (white, with text as below).

Please prepare the design using placeholder text. I will work with the winning submission to complete the final information in the last iteration.

To give you a sense of her services a profile is below:
- I offer an integrative approach for effective relief of many issues such as anxiety, panic attacks, relationship difficulties, and health problems. In my counselling sessions I mainly use QBR {Quiet Balance Release } which taps into the body's energy system (meridians) to clear up blockages and limiting /distorted thinking and beliefs. I also work on expanding awareness as well as enhancing relationships.Clients have found the sessions life changing and report feeling lighter, clearer more empowered and connected to themselves and others.

Target Market(s)

Well educated, upper socioeconomic people seeking purpose and happiness in their lives.

Industry/Entity Type

Health

Requirements
Must have
• Must have the following text on front

First Name, Last Name
LLB, ND, Dip C
Counselling & Naturopathy
Quiet Balnce Release and Marlow Therapy

Adress 1 Line 1
Adress 1 Line 2

Adress 2 Line 1
Adress 2 Line 2

xxx.xxx@xxxxx.com

Tel: 0XXX XXX XXX

Must have the following text on reverse - which should be primarily white.

Next appointment
Date:
Time:
Nice to have
• Example colour palettes

http://www.huebinder.example/swatch/512093/velvet_lantern
http://www.huebinder.example/swatch/318420/Quiet_Orchard
http://www.huebinder.example/swatch/607215/Morning_Over_Tides

Example images that may be useful...
http://www.shopvarn.example/gp/product/images/4719205536/ref=dp_image_text_0?ie=UTF8&n=517302&s=books
http://www.shopvarn.example/gp/customer-media/product-gallery/6284019573/ref=cm_ciu_pdp_images_all
http://en.loreweb.example/wiki/File:Lotus_Grid_256bw.gif

```html
<!DOCTYPE html>
<html lang="en">
<head>
<meta charset="utf-8">
<title>Business Card – Front and Back</title>
<link rel="stylesheet" href="https://fonts.googleapis.com/css2?family=Source+Sans+3:wght@400;600;700&family=Italianno&display=swap">
<style>
  :root {
    --backdrop: #c9c9c9;
    --bark: #533c31;
    --cream: #f5f1b8;
    --cream-soft: #ebe29a;
    --olive: #c8c23c;
    --paper: #f8f7ef;
    --rule: #8d8a84;
    --ribbon-ink: #f8f4ea;
    --ornament-faint: #f3efc4;
  }
  * { margin: 0; padding: 0; box-sizing: border-box; }
  html, body {
    width: 1200px; height: 898px; overflow: hidden;
    background: var(--backdrop);
  }
  .canvas {
    position: relative; width: 1200px; height: 898px;
    display: flex; flex-direction: column; align-items: center; justify-content: center; gap: 44px;
  }
  .card {
    position: relative; width: 640px; height: 366px;
    box-shadow: 0 6px 18px rgba(0,0,0,.18);
    overflow: hidden;
  }

  /* Back: appointment card */
  .card--back { background: var(--paper); }
  .back-ornament { position: absolute; left: 150px; top: 110px; }
  .ribbon { position: absolute; left: 150px; top: 28px; }
  .ribbon-title {
    position: absolute; left: 150px; top: 28px; width: 420px; height: 40px;
    display: flex; align-items: center; justify-content: center;
    font-family: "Italianno", cursive; font-weight: 400; font-size: 34px; letter-spacing: 1px;
    color: var(--ribbon-ink);
  }
  .write-lines { position: absolute; left: 40px; right: 40px; top: 100px; }
  .write-lines span { display: block; height: 34px; border-bottom: 1px solid var(--rule); }

  /* Front: contact card */
  .card--front { background: var(--bark); color: var(--cream); font-family: "Source Sans 3", sans-serif; }
  .ornament-row { position: absolute; left: 0; top: 0; }
  .identity { position: absolute; left: 0; right: 0; top: 168px; text-align: center; }
  .identity-name { font-size: 24px; font-weight: 700; color: var(--cream); line-height: 1.1; }
  .identity-creds { font-size: 17px; font-weight: 400; color: var(--cream); margin-top: 2px; }
  .services {
    font-family: "Italianno", cursive; color: var(--cream-soft);
    font-size: 26px; line-height: 0.95; margin-top: 8px;
  }
  .contact {
    position: absolute; left: 44px; right: 40px; top: 284px;
    display: grid; grid-template-columns: 1.25fr 1.25fr 1.5fr;
    font-size: 15.5px; line-height: 1.3; color: var(--cream);
    font-style: normal;
  }
  .contact-block--reach { padding-top: 20px; }
</style>
</head>
<body>
<main class="canvas">

  <section class="card card--back" aria-label="Appointment card, back">
    <svg class="back-ornament" width="160" height="160" viewBox="0 0 160 160" role="img" aria-label="Faint mandala ornament behind the writing lines">
      <circle cx="80" cy="80" r="78" fill="var(--ornament-faint)"/>
    </svg>
    <div class="write-lines" aria-hidden="true">
      <span></span><span></span><span></span><span></span><span></span><span></span><span></span>
    </div>
    <svg class="ribbon" width="420" height="40" viewBox="0 0 420 40" aria-hidden="true">
      <polygon points="0,0 420,0 404,20 420,40 0,40 16,20" fill="var(--bark)"/>
    </svg>
    <h2 class="ribbon-title">Your Next Appointment</h2>
  </section>

  <section class="card card--front" aria-label="Business card, front">
    <svg class="ornament-row" width="640" height="200" viewBox="0 0 640 200" role="img" aria-label="Row of seven pale yellow mandala ornaments, largest in the centre">
      <circle cx="52"  cy="140" r="24" fill="var(--cream)"/>
      <circle cx="122" cy="110" r="34" fill="var(--cream)"/>
      <circle cx="210" cy="90"  r="40" fill="var(--cream)"/>
      <circle cx="312" cy="82"  r="52" fill="var(--cream)"/>
      <circle cx="418" cy="100" r="40" fill="var(--cream)"/>
      <circle cx="510" cy="126" r="34" fill="var(--cream)"/>
      <circle cx="584" cy="150" r="26" fill="var(--cream)"/>
    </svg>

    <div class="identity">
      <h1 class="identity-name">Name Surname</h1>
      <p class="identity-creds">LLB, ND, Dip C</p>
      <p class="services">Counselling &amp; Naturopathy<br>Quiet Balnce Release and Marlow Therapy</p>
    </div>

    <address class="contact">
      <p class="contact-block">Adress 1 Line 1<br>Adress 1 Line 2</p>
      <p class="contact-block">Adress 2 Line 1<br>Adress 2 Line 2</p>
      <p class="contact-block contact-block--reach">E:xxx.xxx@xxxxx.com<br>T: 0XXX XXX XXX</p>
    </address>
  </section>

</main>
</body>
</html>
```